Keystone Prime Water Tank

I primarily market the water tanks so want a business care that reflects that. I have attached the water tank logo. You have been working on our water tank so maybe we can use that on the card et. I am leaving as one sided but can be double sided if that works. The information that needs to be on the cards is as follows: Gerald T. Munro Phone numbers: Office 555-284-9137 Direct 555-619-2405 Mobile 555-372-5841 email address: gerald@fieldgearworks.com Address P.O. Box 8273 Lakeridge, OH 30512 Web Page: www.fieldgearworks.com. A lot to fit on the card. Thanks

```html
<!DOCTYPE html>
<html lang="en">
<head>
<meta charset="utf-8">
<title>Gerald T. Munro – Business Card</title>
<link rel="stylesheet" href="https://fonts.googleapis.com/css2?family=Roboto:wght@400;700&family=Roboto+Condensed:wght@700&display=swap">
<style>
  :root {
    --red: #e3141b;
    --black: #0b0b0b;
    --white: #ffffff;
    --backdrop: #ffffff;
    --ink: #1a1a1a;
  }
  * { box-sizing: border-box; margin: 0; padding: 0; }
  html, body { width: 1200px; height: 1200px; overflow: hidden; background: var(--backdrop); }
  .stage {
    width: 1200px; height: 1200px;
    display: flex; align-items: center; justify-content: center; gap: 50px;
  }
  .card {
    position: relative; width: 540px; height: 310px;
    background: var(--black);
    box-shadow: 4px 5px 8px rgba(0,0,0,.35);
    overflow: hidden;
    font-family: "Roboto", Arial, sans-serif;
  }
  .edge-black { position: absolute; left: 0; top: 0; width: 5px; height: 100%; background: var(--black); }
  .edge-red { position: absolute; left: 5px; top: 0; width: 7px; height: 100%; background: var(--red); }
  .edge-white { position: absolute; left: 12px; top: 0; width: 4px; height: 100%; background: var(--white); }
  .logo-panel {
    position: absolute; left: 16px; top: 0; width: 104px; height: 100%;
    background: var(--white);
    display: flex; flex-direction: column; align-items: center; justify-content: center; gap: 6px;
    padding-top: 40px;
  }
  .logo-mark { width: 18px; height: 18px; border-radius: 50%; background: var(--red); }
  .logo-name {
    font-weight: 700; font-size: 11px; line-height: 1.2; color: var(--ink);
    text-align: center; text-transform: uppercase;
  }
  .name-band {
    position: absolute; left: 120px; top: 0; right: 0; height: 74px;
    background: var(--white);
    border-top: 7px solid var(--red);
    border-bottom: 4px solid var(--red);
  }
  .name {
    position: absolute; left: 0; top: 10px;
    font-family: "Roboto Condensed", "Arial Narrow", sans-serif;
    font-weight: 700; font-size: 42px; letter-spacing: .3px; color: var(--red);
    text-transform: uppercase; line-height: 1;
  }
  .contacts {
    position: absolute; left: 148px; top: 92px; list-style: none;
    color: var(--white); font-size: 18.5px; line-height: 26px;
  }
  .contacts li { display: flex; align-items: center; gap: 7px; white-space: nowrap; }
  .contacts .icon { width: 17px; height: 17px; flex: none; }
  .contacts .spacer { width: 17px; flex: none; }
  .contacts strong { font-weight: 700; margin-right: 5px; }
  .foot-stripes { position: absolute; left: 120px; right: 0; bottom: 26px; }
  .foot-stripes .red { height: 6px; background: var(--red); }
  .foot-stripes .white { height: 5px; background: var(--white); }
</style>
</head>
<body>
<main class="stage">
  <section class="card" aria-label="Business card front">
    <div class="edge-black"></div><div class="edge-red"></div><div class="edge-white"></div>
    <div class="logo-panel">
      <span class="logo-mark"></span>
      <span class="logo-name">Keystone Prime<br>Water Tank</span>
    </div>
    <header class="name-band"><h1 class="name">Gerald T. Munro</h1></header>
    <ul class="contacts">
      <li><svg class="icon" viewBox="0 0 20 20"><circle cx="10" cy="10" r="10" fill="#e3141b"/><path d="M5 10.5 10 6l5 4.5h-1.6V14H6.6v-3.5z" fill="#0b0b0b"/></svg>P.O. Box 8273 Lakeridge, OH 30512</li>
      <li><svg class="icon" viewBox="0 0 20 20"><circle cx="10" cy="10" r="10" fill="#e3141b"/><path d="M6.5 5.5c1-.6 1.5 0 2 1l.5 1.2c.2.6-.6 1-.6 1.4.4 1.2 1.4 2.2 2.5 2.6.4 0 .8-.8 1.4-.6l1.2.5c1 .5 1.6 1 1 2-1 1.4-3 1.2-5-.4S5 7.7 6.5 5.5z" fill="#0b0b0b"/></svg><strong>OFFICE</strong>555-284-9137</li>
      <li><span class="spacer"></span><strong>DIRECT</strong>555-619-2405</li>
      <li><svg class="icon" viewBox="0 0 20 20"><circle cx="10" cy="10" r="10" fill="#e3141b"/><rect x="7" y="4.5" width="6" height="11" rx="1.2" fill="#0b0b0b"/><rect x="8" y="6" width="4" height="7" fill="#e3141b"/></svg>555-372-5841</li>
      <li><svg class="icon" viewBox="0 0 20 20"><circle cx="10" cy="10" r="10" fill="#e3141b"/><rect x="5" y="6.5" width="10" height="7" fill="#0b0b0b"/><path d="M5 6.5l5 4 5-4" stroke="#e3141b" stroke-width="1" fill="none"/></svg>gerald@fieldgearworks.com</li>
      <li><svg class="icon" viewBox="0 0 20 20"><circle cx="10" cy="10" r="10" fill="#e3141b"/><g fill="none" stroke="#0b0b0b" stroke-width="1.2"><circle cx="10" cy="10" r="5.5"/><ellipse cx="10" cy="10" rx="2.3" ry="5.5"/><path d="M4.5 10h11"/></g></svg>www.fieldgearworks.com</li>
    </ul>
    <div class="foot-stripes"><div class="red"></div><div class="white"></div><div class="red"></div></div>
  </section>

  <section class="card" aria-label="Business card back">
    <div class="edge-black"></div><div class="edge-red"></div><div class="edge-white"></div>
    <div class="logo-panel">
      <span class="logo-mark"></span>
      <span class="logo-name">Keystone Prime<br>Water Tank</span>
    </div>
    <header class="name-band"><h2 class="name">Gerald T. Munro</h2></header>
    <ul class="contacts">
      <li><svg class="icon" viewBox="0 0 20 20"><circle cx="10" cy="10" r="10" fill="#e3141b"/><path d="M5 10.5 10 6l5 4.5h-1.6V14H6.6v-3.5z" fill="#0b0b0b"/></svg>P.O. Box 8273 Lakeridge, OH 30512</li>
      <li><svg class="icon" viewBox="0 0 20 20"><circle cx="10" cy="10" r="10" fill="#e3141b"/><path d="M6.5 5.5c1-.6 1.5 0 2 1l.5 1.2c.2.6-.6 1-.6 1.4.4 1.2 1.4 2.2 2.5 2.6.4 0 .8-.8 1.4-.6l1.2.5c1 .5 1.6 1 1 2-1 1.4-3 1.2-5-.4S5 7.7 6.5 5.5z" fill="#0b0b0b"/></svg><strong>OFFICE</strong>555-284-9137</li>
      <li><span class="spacer"></span><strong>DIRECT</strong>555-619-2405</li>
      <li><svg class="icon" viewBox="0 0 20 20"><circle cx="10" cy="10" r="10" fill="#e3141b"/><rect x="7" y="4.5" width="6" height="11" rx="1.2" fill="#0b0b0b"/><rect x="8" y="6" width="4" height="7" fill="#e3141b"/></svg>555-372-5841</li>
      <li><svg class="icon" viewBox="0 0 20 20"><circle cx="10" cy="10" r="10" fill="#e3141b"/><rect x="5" y="6.5" width="10" height="7" fill="#0b0b0b"/><path d="M5 6.5l5 4 5-4" stroke="#e3141b" stroke-width="1" fill="none"/></svg>gerald@fieldgearworks.com</li>
      <li><svg class="icon" viewBox="0 0 20 20"><circle cx="10" cy="10" r="10" fill="#e3141b"/><g fill="none" stroke="#0b0b0b" stroke-width="1.2"><circle cx="10" cy="10" r="5.5"/><ellipse cx="10" cy="10" rx="2.3" ry="5.5"/><path d="M4.5 10h11"/></g></svg>www.fieldgearworks.com</li>
    </ul>
    <div class="foot-stripes"><div class="red"></div><div class="white"></div><div class="red"></div></div>
  </section>
</main>
</body>
</html>
```